Exterior cleaning company requires a eye catching a5 leaflet

we need some updated leaflet designs, a5 folded, we are targeting all exterior cleaning contracts, including roof cleaning & treatment, render cleaning & Treatment, driveways, block paving cleaning using the latest in low pressure cleaning technologies along side high pressure jetwashing. gutter clearance and flushing, water fed telescopic pole window cleaning of difficult to reach windows and high buildings. our website : www.tkbellowsec.co.uk facebook page: https://www.facebook.com/tkbellowsexteriorcareltd Instagram: https://www.instagram.com/tkbellowsec/ a quick google search of roof cleaning, soft washing etc will provide results of what we are doing

Target Market(s)

home owners, commercial clients

Font styles to use
Serif
Sans Serif

Requirements
Must have
• A5 Landscape folded leaflet, front page with company information and bullet points of main works : window & conservatory cleaning, roof cleaning & treatment, Render cleaning & treatment, pressure washing, soft washing, gutter clearing, pressure washing of patios, driveways, gutters, fascias (more info can be provided on techniques etc if required)

```html
<!DOCTYPE html>
<html lang="en">
<head>
<meta charset="utf-8">
<title>TK Bellows Exterior Care – A5 Leaflet</title>
<link href="https://fonts.googleapis.com/css2?family=Arimo:wght@400;700&family=Roboto:wght@300;700&display=swap" rel="stylesheet">
<style>
:root{
  --navy:#13294b;
  --navy-deep:#0c1d38;
  --orange:#f07c12;
  --white:#ffffff;
  --ink:#333a44;
  --backdrop:#a9672f;
  --brick:#8a4a35;
  --glass:#4f7f97;
}
*{margin:0;padding:0;box-sizing:border-box}
html,body{width:1200px;height:907px;overflow:hidden}
body{background:var(--backdrop);font-family:"Arimo",Arial,sans-serif;color:var(--ink)}
.sheet{position:relative;width:1200px;height:907px;overflow:hidden}
.label{position:absolute;font-family:"Arimo",Arial,sans-serif;font-weight:700;color:#111;font-size:40px;line-height:1}
.label--option{left:860px;top:124px}
.label--front{left:147px;top:327px}
.label--back{left:627px;top:450px}
.label--inside{left:930px;top:741px}

.card{position:absolute;overflow:hidden;background:var(--white);box-shadow:0 3px 10px rgba(0,0,0,.45)}
.card svg.card__art{position:absolute;left:0;top:0}
.card--front{left:32px;top:24px;width:374px;height:268px}
.card--option{left:440px;top:24px;width:376px;height:268px}
.card--back{left:776px;top:312px;width:376px;height:268px}
.card--inside{left:32px;top:594px;width:840px;height:298px}

.brand{position:absolute;display:flex;align-items:center;gap:8px}
.brand__mark{width:38px;height:38px;border-radius:50%;border:1.5px solid var(--navy)}
.brand__name{font-family:"Arimo",sans-serif;font-weight:700;color:var(--navy);font-size:12px;line-height:1.1}
.brand__tel{font-size:8px;color:var(--navy);margin-top:2px}
.card--front .brand,.card--option .brand{left:30px;top:20px}

.headline{position:absolute;left:20px;top:103px;color:var(--white);font-family:"Roboto",sans-serif;line-height:1}
.headline__small{display:block;font-weight:300;font-size:22px;letter-spacing:.3px}
.headline__big{display:block;font-weight:700;font-size:26px;margin-top:2px}

.services-row{position:absolute;left:8px;right:8px;top:194px;display:flex;justify-content:space-between}
.service-icon{width:58px;text-align:center;font-size:5.5px;line-height:1.25;font-weight:700}
.service-icon svg{display:block;margin:0 auto 3px}
.card--front .service-icon{color:var(--navy)}
.card--front .service-icon span{color:var(--orange)}
.card--option .service-icon{color:var(--white)}

.back-brand{position:absolute;left:14px;top:152px;display:flex;align-items:center;gap:6px}
.back-brand .brand__mark{width:22px;height:22px;border-color:var(--white)}
.back-brand .brand__name{color:var(--white);font-size:7px}
.back-brand .brand__tel{color:var(--white);font-size:4.5px}
.back-rule{position:absolute;left:14px;top:178px;width:98px;height:1px;background:rgba(255,255,255,.5)}
.contact{position:absolute;left:14px;color:var(--white);font-size:6.6px;line-height:1.35;display:flex;gap:5px}
.contact i{display:block;width:6px;height:6px;margin-top:1px;background:var(--orange);border-radius:1px;flex:none}

.pill{position:absolute;height:18px;border-radius:0 9px 9px 0;font-weight:700;font-size:13px;line-height:18px;padding:0 14px 0 12px}
.pill--about{left:142px;top:23px;background:var(--white);color:var(--navy)}
.pill--services{left:452px;top:23px;background:var(--navy);color:var(--white)}
.about-copy{position:absolute;left:153px;top:52px;width:248px;color:var(--white);font-size:6.5px;line-height:8.5px}
.about-copy p{margin-bottom:5.5px}
.about-copy p.indent{padding-left:7px}
.about-copy p.indent2{padding-left:11px}
.service-list{position:absolute;left:466px;top:51px;width:362px}
.service-item{position:relative;padding-left:50px;margin-bottom:8px}
.service-item svg{position:absolute;left:0;top:4px}
.service-item h3{font-size:7.6px;font-weight:700;color:var(--navy);line-height:10px}
.service-item p{font-size:6.5px;line-height:8.3px;color:var(--ink)}
</style>
</head>
<body>
<div class="sheet">

  <div class="label label--option">Front option</div>
  <div class="label label--front">Front</div>
  <div class="label label--back">Back</div>
  <div class="label label--inside">Inside</div>

  <section class="card card--front">
    <svg class="card__art" width="374" height="268" viewBox="0 0 374 268">
      <defs>
        <linearGradient id="photoFront" x1="0" y1="0" x2="0" y2="1">
          <stop offset="0" stop-color="var(--glass)"/><stop offset=".6" stop-color="var(--brick)"/><stop offset="1" stop-color="#9a8d7e"/>
        </linearGradient>
      </defs>
      <path d="M0,78 C110,82 210,72 290,40 L290,54 C210,88 110,98 0,96 Z" fill="var(--orange)"/>
      <path d="M0,96 C110,98 210,88 290,54 L374,40 L374,158 C290,196 170,206 0,178 Z" fill="var(--navy)"/>
      <path d="M0,178 C170,206 290,196 374,158 L374,172 C290,214 160,214 0,190 Z" fill="var(--orange)"/>
      <circle cx="318" cy="72" r="106" fill="var(--orange)"/>
      <circle cx="318" cy="72" r="101" fill="var(--white)"/>
      <circle cx="318" cy="72" r="98" fill="url(#photoFront)" role="img" aria-label="Photo: operative cleaning the glass front of a brick office building with a water fed pole"/>
      <rect x="0" y="251" width="374" height="17" fill="var(--orange)"/>
    </svg>
    <div class="brand">
      <div class="brand__mark"></div>
      <div>
        <div class="brand__name">TK Bellows<br>Exterior Care Ltd</div>
        <div class="brand__tel">Tel: 01632 960 418</div>
      </div>
    </div>
    <h1 class="headline"><span class="headline__small">OVER 10 YEARS</span><span class="headline__big">EXPERIENCE</span></h1>
    <div class="services-row">
      <div class="service-icon"><svg width="28" height="28" viewBox="0 0 28 28"><circle cx="14" cy="14" r="12.5" fill="none" stroke="var(--navy)" stroke-width="1.5"/><path d="M8,20 L19,9 M15,19 L20,14" stroke="var(--navy)" stroke-width="1.8"/></svg><span>Window &amp;</span><br><span>Conservatory Cleaning</span></div>
      <div class="service-icon"><svg width="28" height="28" viewBox="0 0 28 28"><circle cx="14" cy="14" r="12.5" fill="none" stroke="var(--navy)" stroke-width="1.5"/><path d="M7,18 L12,10 L21,10 L21,18 Z M10,18 L14,12" fill="none" stroke="var(--navy)" stroke-width="1.4"/></svg><span>Roof Cleaning</span><br><span>&amp; Treatment</span></div>
      <div class="service-icon"><svg width="28" height="28" viewBox="0 0 28 28"><circle cx="14" cy="14" r="12.5" fill="none" stroke="var(--navy)" stroke-width="1.5"/><path d="M18,7 L13,16 M9,16 L17,16 L15,21 L8,21 Z" fill="none" stroke="var(--navy)" stroke-width="1.5"/></svg><span>Render Cleaning</span><br><span>&amp; Treatment</span></div>
      <div class="service-icon"><svg width="28" height="28" viewBox="0 0 28 28"><circle cx="14" cy="14" r="12.5" fill="none" stroke="var(--navy)" stroke-width="1.5"/><path d="M10,7 L10,21 M10,7 L15,7 M16,13 L19,13 L19,21 L15,21 Z" fill="none" stroke="var(--navy)" stroke-width="1.5"/></svg><span>Pressure</span><br><span>Washing</span></div>
      <div class="service-icon"><svg width="28" height="28" viewBox="0 0 28 28"><circle cx="14" cy="14" r="12.5" fill="none" stroke="var(--navy)" stroke-width="1.5"/><path d="M8,15 L20,15 L18,21 L10,21 Z" fill="none" stroke="var(--navy)" stroke-width="1.5"/><circle cx="12" cy="11" r="2" fill="none" stroke="var(--navy)"/><circle cx="17" cy="10" r="1.5" fill="none" stroke="var(--navy)"/></svg><span>Soft</span><br><span>Washing</span></div>
      <div class="service-icon"><svg width="28" height="28" viewBox="0 0 28 28"><circle cx="14" cy="14" r="12.5" fill="none" stroke="var(--navy)" stroke-width="1.5"/><path d="M7,10 L21,10 L21,14 Q21,18 17,18 L11,18 L11,21" fill="none" stroke="var(--navy)" stroke-width="1.5"/></svg><span>Gutter</span><br><span>Clearing</span></div>
    </div>
  </section>

  <section class="card card--option">
    <svg class="card__art" width="376" height="268" viewBox="0 0 376 268">
      <defs>
        <linearGradient id="photoOption" x1="0" y1="0" x2="0" y2="1">
          <stop offset="0" stop-color="var(--glass)"/><stop offset=".6" stop-color="var(--brick)"/><stop offset="1" stop-color="#9a8d7e"/>
        </linearGradient>
      </defs>
      <path d="M0,78 C110,82 210,72 290,40 L290,54 C210,88 110,98 0,96 Z" fill="var(--orange)"/>
      <path d="M0,96 C110,98 210,88 290,54 L376,40 L376,158 C290,196 170,206 0,178 Z" fill="var(--navy)"/>
      <path d="M0,178 C170,206 290,196 376,158 L376,268 L0,268 Z" fill="var(--orange)"/>
      <path d="M0,178 C170,206 290,196 376,158 L376,166 C290,206 170,214 0,188 Z" fill="var(--white)"/>
      <circle cx="320" cy="72" r="106" fill="var(--orange)"/>
      <circle cx="320" cy="72" r="101" fill="var(--white)"/>
      <circle cx="320" cy="72" r="98" fill="url(#photoOption)" role="img" aria-label="Photo: operative cleaning the glass front of a brick office building with a water fed pole"/>
      <rect x="0" y="246" width="376" height="22" fill="var(--navy)"/>
    </svg>
    <div class="brand">
      <div class="brand__mark"></div>
      <div>
        <div class="brand__name">TK Bellows<br>Exterior Care Ltd</div>
        <div class="brand__tel">Tel: 01632 960 418</div>
      </div>
    </div>
    <h1 class="headline"><span class="headline__small">OVER 10 YEARS</span><span class="headline__big">EXPERIENCE</span></h1>
    <div class="services-row">
      <div class="service-icon"><svg width="28" height="28" viewBox="0 0 28 28"><circle cx="14" cy="14" r="12.5" fill="none" stroke="var(--white)" stroke-width="1.5"/><path d="M8,20 L19,9 M15,19 L20,14" stroke="var(--white)" stroke-width="1.8"/></svg>Window &amp;<br>Conservatory Cleaning</div>
      <div class="service-icon"><svg width="28" height="28" viewBox="0 0 28 28"><circle cx="14" cy="14" r="12.5" fill="none" stroke="var(--white)" stroke-width="1.5"/><path d="M7,18 L12,10 L21,10 L21,18 Z M10,18 L14,12" fill="none" stroke="var(--white)" stroke-width="1.4"/></svg>Roof Cleaning<br>&amp; Treatment</div>
      <div class="service-icon"><svg width="28" height="28" viewBox="0 0 28 28"><circle cx="14" cy="14" r="12.5" fill="none" stroke="var(--white)" stroke-width="1.5"/><path d="M18,7 L13,16 M9,16 L17,16 L15,21 L8,21 Z" fill="none" stroke="var(--white)" stroke-width="1.5"/></svg>Render Cleaning<br>&amp; Treatment</div>
      <div class="service-icon"><svg width="28" height="28" viewBox="0 0 28 28"><circle cx="14" cy="14" r="12.5" fill="none" stroke="var(--white)" stroke-width="1.5"/><path d="M10,7 L10,21 M10,7 L15,7 M16,13 L19,13 L19,21 L15,21 Z" fill="none" stroke="var(--white)" stroke-width="1.5"/></svg>Pressure<br>Washing</div>
      <div class="service-icon"><svg width="28" height="28" viewBox="0 0 28 28"><circle cx="14" cy="14" r="12.5" fill="none" stroke="var(--white)" stroke-width="1.5"/><path d="M8,15 L20,15 L18,21 L10,21 Z" fill="none" stroke="var(--white)" stroke-width="1.5"/><circle cx="12" cy="11" r="2" fill="none" stroke="var(--white)"/><circle cx="17" cy="10" r="1.5" fill="none" stroke="var(--white)"/></svg>Soft<br>Washing</div>
      <div class="service-icon"><svg width="28" height="28" viewBox="0 0 28 28"><circle cx="14" cy="14" r="12.5" fill="none" stroke="var(--white)" stroke-width="1.5"/><path d="M7,10 L21,10 L21,14 Q21,18 17,18 L11,18 L11,21" fill="none" stroke="var(--white)" stroke-width="1.5"/></svg>Gutter<br>Clearing</div>
    </div>
  </section>

  <section class="card card--back">
    <svg class="card__art" width="376" height="268" viewBox="0 0 376 268">
      <defs>
        <linearGradient id="photoBack" x1="0" y1="0" x2="1" y2="1">
          <stop offset="0" stop-color="#6e6e6e"/><stop offset=".5" stop-color="#9a9a9a"/><stop offset="1" stop-color="#d4d4d4"/>
        </linearGradient>
        <linearGradient id="navyBack" x1="0" y1="0" x2="1" y2="0">
          <stop offset="0" stop-color="var(--navy-deep)"/><stop offset="1" stop-color="var(--navy)"/>
        </linearGradient>
      </defs>
      <rect width="376" height="200" fill="url(#photoBack)" role="img" aria-label="Black and white photo: large brick house with a white company van parked outside"/>
      <path d="M0,140 C80,138 170,150 240,170 C300,188 340,190 376,178 L376,268 L0,268 Z" fill="url(#navyBack)"/>
      <path d="M200,148 C270,170 320,178 376,150 L376,162 C320,192 270,186 220,168 Z" fill="var(--orange)"/>
      <path d="M230,168 C290,186 330,190 376,170 L376,176 C330,198 290,194 240,174 Z" fill="var(--white)"/>
    </svg>
    <div class="back-brand">
      <div class="brand__mark"></div>
      <div>
        <div class="brand__name">TK Bellows<br>Exterior Care Ltd</div>
        <div class="brand__tel">Tel: 01632 960 418</div>
      </div>
    </div>
    <div class="back-rule"></div>
    <div class="contact" style="top:186px"><i></i><span>14 Marram Close,<br>Southport, PR9 4ZZ</span></div>
    <div class="contact" style="top:211px"><i></i><span>01632 960 418</span></div>
    <div class="contact" style="top:228px"><i></i><span>info@tkbellowsec.co.uk<br>http://www.tkbellowsec.co.uk/</span></div>
  </section>

  <section class="card card--inside">
    <svg class="card__art" width="840" height="298" viewBox="0 0 840 298">
      <defs>
        <linearGradient id="photoInside" x1="0" y1="0" x2="0" y2="1">
          <stop offset="0" stop-color="#9b5643"/><stop offset=".6" stop-color="var(--brick)"/><stop offset="1" stop-color="#5a4a40"/>
        </linearGradient>
        <linearGradient id="servicesBg" x1="0" y1="0" x2="1" y2="0">
          <stop offset="0" stop-color="var(--white)"/><stop offset="1" stop-color="#dcdcdc"/>
        </linearGradient>
        <linearGradient id="circleA" x1="0" y1="0" x2="1" y2="1"><stop offset="0" stop-color="#b8a890"/><stop offset="1" stop-color="#7b6e5c"/></linearGradient>
        <linearGradient id="circleB" x1="0" y1="0" x2="0" y2="1"><stop offset="0" stop-color="#6fa4d4"/><stop offset="1" stop-color="#d9d7d2"/></linearGradient>
        <linearGradient id="circleC" x1="0" y1="0" x2="0" y2="1"><stop offset="0" stop-color="#8b7b6c"/><stop offset="1" stop-color="#3e3a35"/></linearGradient>
        <linearGradient id="circleD" x1="0" y1="0" x2="1" y2="1"><stop offset="0" stop-color="#7a8a5a"/><stop offset="1" stop-color="#4a4f3c"/></linearGradient>
      </defs>
      <rect width="840" height="298" fill="url(#servicesBg)"/>
      <rect width="170" height="298" fill="url(#photoInside)" role="img" aria-label="Photo: operative cleaning the upper windows of a red brick house"/>
      <path d="M95,0 C130,40 130,100 125,298 L490,298 L400,0 Z" fill="var(--orange)"/>
      <path d="M110,0 C145,40 140,100 135,298 L482,298 L395,0 Z" fill="var(--white)"/>
      <path d="M122,0 C155,40 150,100 145,298 L475,298 L385,0 Z" fill="var(--navy)"/>
      <path d="M360,0 C420,40 460,120 480,298 L492,298 C470,120 440,40 390,0 Z" fill="var(--orange)"/>
      <path d="M390,0 C440,40 470,120 492,298 L500,298 C480,120 450,40 400,0 Z" fill="var(--white)"/>
      <path d="M365,0 L385,0 C420,40 450,120 475,298 L460,298 C440,120 410,40 365,0 Z" fill="var(--navy)"/>
      <circle cx="110" cy="166" r="40" fill="var(--white)"/><circle cx="110" cy="166" r="37.5" fill="url(#circleA)" role="img" aria-label="Photo: cleaned stone patio"/>
      <circle cx="92" cy="244" r="40" fill="var(--white)"/><circle cx="92" cy="244" r="37.5" fill="url(#circleB)" role="img" aria-label="Photo: cleaned white render on a house"/>
      <circle cx="443" cy="168" r="36" fill="var(--white)"/><circle cx="443" cy="168" r="33.5" fill="url(#circleC)" role="img" aria-label="Photo: clean white fascia and gutter"/>
      <circle cx="442" cy="248" r="38" fill="var(--white)"/><circle cx="442" cy="248" r="35.5" fill="url(#circleD)" role="img" aria-label="Photo: moss being cleared from a gutter"/>
    </svg>
    <div class="pill pill--about">ABOUT US</div>
    <div class="pill pill--services">SERVICES</div>
    <div class="about-copy">
      <p>T.K Bellows Exterior Care is Southport’s most reliable, professional cleaning company who have been providing cleaning services across the North West for 10 years!</p>
      <p>At T.K Bellows, our mission is to lead our sector in providing all of our customers with an outstanding cleaning service that keeps ourselves one step ahead of our competition. All of our staff are uniformed, polite, courteous and always happy to help. We aim to build long lasting relationships with our customers, and offer a 5* customer service team to help resolve any issues that may arise.</p>
      <p class="indent">At T.K Bellows our staff use the reach &amp; wash system, otherwise known as the ‘water fed pole’. A technique which compared to traditional window cleaning, reaches your windows and frames safely from the ground, even in hard to reach areas such as above conservatories or dormer windows. This prevents any damage to your property from equipment and prevents accidents.</p>
      <p class="indent2">We like to keep things simple so our visits to you run as smoothly as possible. We also provide a secure, key holding service if you’d prefer us to be able to lock up after we’ve finished. Our window cleaning round varies from domestic houses to commercial buildings, shops, schools, factories, blocks of flats and much more. Please refer to the ‘services’ page of our website for further information on other aspects of our cleaning.</p>
    </div>
    <div class="service-list">
      <div class="service-item">
        <svg width="20" height="20" viewBox="0 0 20 20"><circle cx="10" cy="10" r="9" fill="none" stroke="var(--navy)" stroke-width="1.2"/><path d="M6,14 L14,6" stroke="var(--navy)" stroke-width="1.4"/></svg>
        <h3>Window &amp; Conservatory Cleaning</h3>
        <p>A technique called ‘water fed pole’ which compared to traditional window cleaning, enabling us to reach your windows and frames safely from the ground. We clean internal windows and mirrors using the dragon fly system using purified method.</p>
      </div>
      <div class="service-item">
        <svg width="20" height="20" viewBox="0 0 20 20"><circle cx="10" cy="10" r="9" fill="none" stroke="var(--navy)" stroke-width="1.2"/><path d="M5,13 L9,7 L15,7 L15,13 Z" fill="none" stroke="var(--navy)" stroke-width="1.1"/></svg>
        <h3>Roof Cleaning &amp; Treatment</h3>
        <p>Has your conservatory roof started to turn green, full of bird muck or dirt? Our water pole method 99% of the time gets rid of all the dirt and grime build up that’s left on your roof.</p>
      </div>
      <div class="service-item">
        <svg width="20" height="20" viewBox="0 0 20 20"><circle cx="10" cy="10" r="9" fill="none" stroke="var(--navy)" stroke-width="1.2"/><path d="M7,5 L7,15 M7,5 L11,5 M11,10 L14,10 L14,15 L11,15 Z" fill="none" stroke="var(--navy)" stroke-width="1.1"/></svg>
        <h3>Pressure Washing</h3>
        <p>We offer a wide range of pressure washing services from garden furniture to house roofs at competitive prices. Cleaning and restoration of all hard surfaces in both the domestic and commercial market.</p>
      </div>
      <div class="service-item">
        <svg width="20" height="20" viewBox="0 0 20 20"><circle cx="10" cy="10" r="9" fill="none" stroke="var(--navy)" stroke-width="1.2"/><path d="M5,7 L15,7 L15,10 Q15,13 12,13 L8,13 L8,16" fill="none" stroke="var(--navy)" stroke-width="1.1"/></svg>
        <h3>Gutter Cleaning</h3>
        <p>Your property’s gutters and downpipes accumulate all sorts of debris brought by the wind. Using our high reach vac we can clean the gutters safely from the ground eliminating any falls from height. Using our telescopic pressure washing lance, we can clean all of your UPVC fascia’s, gutters and drain pipes safely from the ground. From small patio areas to large driveways we clean it all. T.K Bellows specialise in all driveway and patio cleaning from Indian stone, tarmac, concrete flags to block paving.</p>
      </div>
      <div class="service-item">
        <svg width="20" height="20" viewBox="0 0 20 20"><circle cx="10" cy="10" r="9" fill="none" stroke="var(--navy)" stroke-width="1.2"/><path d="M5,13 L7,7 L15,7 L13,13 Z M10,7 L9,13" fill="none" stroke="var(--navy)" stroke-width="1.1"/></svg>
        <h3>Solar Panels</h3>
        <p>Using our access equipment we can clean your solar panels. Anything that blocks the light transmission to your solar PV (or thermal) panels has the potential to lower the performance.</p>
      </div>
    </div>
  </section>

</div>
</body>
</html>
```